Career-focused learning application platform

We have a K-12 learning application platform designed for grades 6-12 that needs user interface improvements that provide a positive experience for all users (teachers and students). The learning platform provides career-focused math curriculum and career exploration resources. We would like to improve the user-interface with engaging design elements without taking away from the functionality and performance of the platform.

```html
<!DOCTYPE html>
<html lang="en">
<head>
<meta charset="utf-8">
<title>StepUp Futures – Teacher Dashboard</title>
<link href="https://fonts.googleapis.com/css2?family=Montserrat:wght@400;500;600;700;800&family=Open+Sans:wght@400;600&display=swap" rel="stylesheet">
<style>
:root{
  --stage:#b3b3b3;
  --white:#ffffff;
  --tint:#f4f1f0;
  --orange:#f07f1a;
  --ink:#1f1f1f;
  --text:#333333;
  --muted:#555555;
  --dark:#2d2c2e;
  --table-head:#434245;
  --row-alt:#eceef0;
  --line:#d9d9d9;
  --btn-dark:#4a4a4d;
}
*{box-sizing:border-box;margin:0;padding:0}
html,body{width:1200px;height:2941px;overflow:hidden}
body{background:var(--stage);font-family:'Montserrat',sans-serif;color:var(--text);position:relative}
.page{position:absolute;left:99px;width:1008px;background:var(--white);overflow:hidden}
.page--dashboard{top:95px;height:1409px}
.page--class{top:1564px;height:1273px}
.abs{position:absolute}

/* header */
.site-header{position:absolute;left:0;top:0;width:100%;height:101px;background:var(--white)}
.brand{position:absolute;left:110px;top:30px;display:flex;align-items:center;gap:8px;color:var(--orange);font-weight:700;font-size:17px;letter-spacing:.2px}
.brand-dot{width:26px;height:26px;border-radius:50%;background:var(--orange)}
.account{position:absolute;right:110px;top:20px;display:flex;align-items:center;gap:20px;font-size:13px;color:var(--ink)}
.avatar{width:29px;height:29px;border-radius:50%;background:var(--orange);display:flex;align-items:center;justify-content:center}
.main-nav{position:absolute;top:64px;left:489px;display:flex;gap:0;font-size:12.5px;color:var(--ink);font-weight:500}
.main-nav span{position:absolute;white-space:nowrap}

/* hero */
.spotlight{position:absolute;top:101px;left:0;width:100%;height:385px;background:var(--tint)}
.spotlight-media{position:absolute;left:493px;top:0;width:515px;height:385px;background:linear-gradient(135deg,#e9eaec 0%,#c9ccd0 45%,#8a7563 75%,#4a5563 100%)}
.play{position:absolute;left:223px;top:164px}
.eyebrow{position:absolute;left:110px;top:31px;font-size:19px;font-weight:800;color:var(--ink);letter-spacing:.2px}
.career-bar{position:absolute;left:110px;top:72px;width:383px;height:36px;background:var(--orange);color:var(--white);font-weight:600;font-size:16px;line-height:36px;padding-left:12px}
.label-sm{position:absolute;left:110px;top:136px;font-size:12px;font-weight:600;color:var(--ink)}
.desc{position:absolute;left:110px;top:160px;width:320px;font-size:12.5px;line-height:18.3px;color:var(--ink)}
.earn-title{position:absolute;left:110px;top:254px;font-size:15px;font-weight:600;color:var(--ink)}
.earn-box{position:absolute;top:286px;width:109px;height:51px;border:1px solid #c9c6c4;padding:9px 0 0 14px}
.earn-box small{display:block;font-size:10px;color:var(--ink)}
.earn-box strong{display:block;font-size:15px;font-weight:500;color:var(--orange);margin-top:2px}

/* classes */
.section-title{position:absolute;font-size:21px;font-weight:800;color:var(--ink)}
.class-card{position:absolute;top:574px;width:247px;height:313px;background:var(--white);box-shadow:0 1px 4px rgba(0,0,0,.18)}
.class-card .thumb{height:161px}
.class-card h3{position:absolute;left:22px;top:179px;font-size:15px;font-weight:600;color:var(--ink)}
.class-card .period{position:absolute;left:22px;top:201px;font-size:12.5px}
.class-card .subject{position:absolute;left:22px;top:227px;font-size:12.5px}
.btn{display:inline-block;background:var(--orange);color:var(--white);font-weight:600;text-align:center}
.class-card .btn{position:absolute;left:22px;top:259px;width:93px;height:23px;line-height:23px;font-size:10px}

/* upcoming */
.upcoming{position:absolute;top:936px;left:0;width:100%;height:360px;background:var(--tint)}
.upcoming h2{position:absolute;top:36px;width:100%;text-align:center;font-size:21px;font-weight:800;color:var(--ink)}
.upcoming p{position:absolute;top:66px;width:100%;text-align:center;font-size:12.5px;color:var(--ink)}
.lesson-table{position:absolute;left:110px;top:116px;width:790px;border-collapse:collapse;font-family:'Open Sans',sans-serif;font-size:13px;box-shadow:0 1px 3px rgba(0,0,0,.15)}
.lesson-table th{background:var(--table-head);color:var(--white);font-family:'Montserrat',sans-serif;font-weight:600;font-size:12px;text-align:left;height:40px}
.lesson-table td{height:40.5px;color:var(--ink);background:var(--white)}
.lesson-table tr:nth-child(even) td{background:var(--row-alt)}
.lesson-table .c1{padding-left:31px;width:249px}
.lesson-table .c2{width:341px}
.lesson-table td.due{color:var(--orange);font-weight:600}

/* footer */
.site-footer{position:absolute;left:0;bottom:0;width:100%;background:var(--dark);color:var(--white)}
.site-footer .links span{position:absolute;font-size:12.5px;white-space:nowrap}
.site-footer .copy{position:absolute;width:100%;text-align:center;font-size:10px}

/* class page */
.back{position:absolute;left:113px;top:127px;font-size:12.5px;color:var(--ink);display:flex;align-items:center;gap:16px}
.class-panel{position:absolute;left:110px;top:161px;width:788px;height:655px;background:var(--white);box-shadow:0 1px 5px rgba(0,0,0,.18)}
.panel-head{height:82px;background:var(--tint);position:relative}
.panel-meta{position:absolute;left:26px;top:18px;font-size:11.5px;line-height:16.8px;color:var(--ink)}
.panel-btn{position:absolute;top:25px;height:32px;width:96px;line-height:32px;font-size:11px;text-align:center;color:var(--white);border-radius:3px}
.panel-btn.dark{left:568px;background:var(--btn-dark)}
.panel-btn.orange{left:672px;background:var(--orange)}
.tabs{position:absolute;left:23px;top:99px;width:745px;height:22px;border-bottom:2px solid var(--line);font-size:11px;color:var(--ink)}
.tabs span{position:absolute;top:0}
.tabs .active{color:var(--orange);border-bottom:2px solid var(--orange);padding-bottom:6px;left:0}
.panel-title{position:absolute;left:25px;top:149px;font-size:16px;color:var(--ink)}
.add-btn{position:absolute;left:693px;top:138px;width:76px;height:25px;line-height:25px;font-size:10px;text-align:center;background:var(--btn-dark);color:var(--white);border-radius:3px}
.lesson-card{position:absolute;left:25px;width:743px;height:96px;border:1px solid #c8c8c8;border-radius:3px;background:var(--white)}
.lesson-card .thumb{position:absolute;left:0;top:0;width:99px;height:94px}
.lesson-card h4{position:absolute;left:120px;top:21px;font-size:12.5px;font-weight:500;color:var(--ink)}
.lesson-card p{position:absolute;left:120px;top:46px;width:380px;font-size:10px;line-height:14.5px;color:var(--ink)}
.lesson-card .due{position:absolute;left:598px;top:20px;font-size:10px;font-weight:600;color:var(--orange)}
.lesson-card .btn{position:absolute;left:601px;top:46px;width:100px;height:27px;line-height:27px;font-size:11px;border-radius:3px}
.lesson-card .gear{position:absolute;left:709px;top:52px}

.promo{position:absolute;top:864px;left:0;width:100%;height:297px;background:var(--tint)}
.promo-media{position:absolute;left:556px;top:0;width:452px;height:297px;background:radial-gradient(circle at 35% 45%,#3aa5e8 0%,#1c5fb8 40%,#0d2550 80%,#0a1a38 100%)}
.promo h2{position:absolute;left:103px;top:50px;font-size:17px;font-weight:600;line-height:21px;color:var(--ink)}
.promo p{position:absolute;left:103px;top:108px;width:410px;font-size:14px;line-height:21.5px;color:var(--ink)}
.promo .btn{position:absolute;left:105px;top:217px;width:115px;height:30px;line-height:30px;font-size:12.5px;border-radius:4px}
</style>
</head>
<body>

<!-- Dashboard -->
<main class="page page--dashboard">
  <header class="site-header">
    <div class="brand"><span class="brand-dot"></span>StepUp Futures</div>
    <div class="account">jo@learnpath.edu
      <span class="avatar"><svg width="13" height="14" viewBox="0 0 13 14"><circle cx="6.5" cy="4" r="3.2" fill="#fff"/><path d="M0.5 14c0-4 2.7-5.8 6-5.8s6 1.8 6 5.8z" fill="#fff"/></svg></span>
    </div>
    <nav class="main-nav"><span style="left:0">HOME</span><span style="left:82px">CAREER TOOLS</span><span style="left:220px">CLASSES</span><span style="left:318px">ASSESSMENTS</span></nav>
  </header>

  <section class="spotlight">
    <div class="eyebrow">CAREER SPOTLIGHT</div>
    <div class="career-bar">Plumbers, Pipefitters, &amp; Streamfitters</div>
    <div class="label-sm">What they do</div>
    <p class="desc">Assemble, install, alter and repair pipelines or pipe systems that carry water, steam, air or other liquids or gases. May install heating and cooling equipment and mechanical control systems.</p>
    <div class="earn-title">Earnings</div>
    <div class="earn-box" style="left:111px"><small>Low End</small><strong>$33,460</strong></div>
    <div class="earn-box" style="left:231px"><small>Median</small><strong>$56,330</strong></div>
    <div class="earn-box" style="left:351px"><small>High End</small><strong>$98,990</strong></div>
    <div class="spotlight-media" role="img" aria-label="Video still of a plumber repairing pipes under a sink">
      <svg class="play" width="50" height="50" viewBox="0 0 50 50"><circle cx="25" cy="25" r="23" fill="#fff" stroke="var(--orange)" stroke-width="4"/><path d="M19 14 L36 25 L19 36z" fill="var(--orange)"/></svg>
    </div>
  </section>

  <h2 class="section-title" style="left:110px;top:523px">CLASSES</h2>
  <article class="class-card" style="left:110px">
    <div class="thumb" role="img" aria-label="Desk of school supplies with a lightbox reading Lets Learn Algebra" style="background:linear-gradient(135deg,#f2c31c,#e9a318 60%,#c7482f)"></div>
    <h3>Math Teacher</h3><div class="period">Period 1</div><div class="subject">8<sup style="font-size:7px">th</sup> Grade Math / Pre-Algebra</div>
    <span class="btn">GO TO CLASS</span>
  </article>
  <article class="class-card" style="left:382px">
    <div class="thumb" role="img" aria-label="Quadratic formula glowing on a blue background" style="background:radial-gradient(circle at 55% 45%,#3b7be0,#163a9a 55%,#0b1d5a)"></div>
    <h3>Math Teacher</h3><div class="period">Period 6</div><div class="subject">Algebra 1</div>
    <span class="btn">GO TO CLASS</span>
  </article>
  <article class="class-card" style="left:651px">
    <div class="thumb" role="img" aria-label="Hand writing equations on a whiteboard" style="background:linear-gradient(135deg,#e6e6e6,#bdbdbd 60%,#8e8e8e)"></div>
    <h3>Math Teacher</h3><div class="period">Period 5</div><div class="subject">Algebra 1</div>
    <span class="btn">GO TO CLASS</span>
  </article>

  <section class="upcoming">
    <h2>UPCOMING LESSONS</h2>
    <p>Lessons due up to the next 7 days</p>
    <table class="lesson-table">
      <tr><th class="c1">CLASS</th><th class="c2">LESSON</th><th>DUE</th></tr>
      <tr><td class="c1">Period 1</td><td>1.1- Translations</td><td class="due">October 5th at 12:00 PM</td></tr>
      <tr><td class="c1">Period 1</td><td>2.1 Operations with rational numbers</td><td class="due">October 12th at 12:00 PM</td></tr>
      <tr><td class="c1">Period 1</td><td>3.1 Parallel Lines and Transverals</td><td class="due">October 21th at 12:00 PM</td></tr>
      <tr><td class="c1">Period 1</td><td>3.3 Angle Relationship in Triangles</td><td class="due">October 30th at 12:00 PM</td></tr>
    </table>
  </section>

  <footer class="site-footer" style="height:113px">
    <div class="links"><span style="left:298px;top:38px">HOME</span><span style="left:381px;top:38px">CAREER TOOLS</span><span style="left:519px;top:38px">CLASSES</span><span style="left:617px;top:38px">ASSESSMENTS</span></div>
    <div class="copy" style="top:72px">Copyright © 2021 All Rights Reserved</div>
  </footer>
</main>

<!-- Class detail -->
<main class="page page--class">
  <header class="site-header">
    <div class="brand"><span class="brand-dot"></span>StepUp Futures</div>
    <div class="account">jo@learnpath.edu
      <span class="avatar"><svg width="13" height="14" viewBox="0 0 13 14"><circle cx="6.5" cy="4" r="3.2" fill="#fff"/><path d="M0.5 14c0-4 2.7-5.8 6-5.8s6 1.8 6 5.8z" fill="#fff"/></svg></span>
    </div>
    <nav class="main-nav"><span style="left:0">HOME</span><span style="left:82px">CAREER TOOLS</span><span style="left:220px">CLASSES</span><span style="left:318px">ASSESSMENTS</span></nav>
  </header>

  <div class="back"><svg width="7" height="11" viewBox="0 0 7 11"><path d="M6 1 L1.5 5.5 L6 10" fill="none" stroke="#222" stroke-width="1.5"/></svg>Browse All Classes</div>

  <section class="class-panel">
    <div class="panel-head">
      <div class="panel-meta">Math Teacher<br>Period 1<br>8th Grade Math / Pre Algebra</div>
      <span class="panel-btn dark">Class Roster</span>
      <span class="panel-btn orange">Class Settings</span>
    </div>
    <div class="tabs"><span class="active">Lessons</span><span style="left:67px">Scores</span></div>
    <h2 class="panel-title">Upcoming Lessons</h2>
    <span class="add-btn">Add Lessons</span>

    <article class="lesson-card" style="top:196px">
      <div class="thumb" role="img" aria-label="Digital interface with holographic icons" style="background:linear-gradient(135deg,#1c3e5c,#2b7fb0 55%,#0f2338)"></div>
      <h4>1.1 Translations</h4>
      <p>Career spotlight: Aerospace Engineer,s Civil Engineers, Aerospace Technicans, Carpernters, Interior Decorators</p>
      <span class="due">Due : 10/15 at 11:59 PM</span><span class="btn">Begin Lesson</span>
      <svg class="gear" width="13" height="13" viewBox="0 0 24 24"><path fill="#333" d="M12 8a4 4 0 1 0 0 8a4 4 0 0 0 0-8zm9.4 5.5l2.1 1.6-2 3.5-2.5-1a8 8 0 0 1-2.3 1.3L16.3 22h-4l-.4-2.6a8 8 0 0 1-2.3-1.3l-2.5 1-2-3.5 2.1-1.6a8 8 0 0 1 0-2.6L5.1 9.8l2-3.5 2.5 1a8 8 0 0 1 2.3-1.3L12.3 3h4l.4 2.6a8 8 0 0 1 2.3 1.3l2.5-1 2 3.5-2.1 1.6a8 8 0 0 1 0 2.6z" transform="translate(-2.3 -0.5)"/></svg>
    </article>
    <article class="lesson-card" style="top:306px">
      <div class="thumb" role="img" aria-label="Hands working with a pen on paper charts" style="background:linear-gradient(135deg,#dfe6ee,#b9c7d6 55%,#d9a98a)"></div>
      <h4>2.1: Operations With Rational Numbers</h4>
      <p>Career Spotlight: Statisticians, Bank Tellers, Nutritionists, Cabinetmaker, Physician</p>
      <span class="due">Due : 10/15 at 11:59 PM</span><span class="btn">Begin Lesson</span>
      <svg class="gear" width="13" height="13" viewBox="0 0 24 24"><path fill="#333" d="M12 8a4 4 0 1 0 0 8a4 4 0 0 0 0-8zm9.4 5.5l2.1 1.6-2 3.5-2.5-1a8 8 0 0 1-2.3 1.3L16.3 22h-4l-.4-2.6a8 8 0 0 1-2.3-1.3l-2.5 1-2-3.5 2.1-1.6a8 8 0 0 1 0-2.6L5.1 9.8l2-3.5 2.5 1a8 8 0 0 1 2.3-1.3L12.3 3h4l.4 2.6a8 8 0 0 1 2.3 1.3l2.5-1 2 3.5-2.1 1.6a8 8 0 0 1 0 2.6z" transform="translate(-2.3 -0.5)"/></svg>
    </article>
    <article class="lesson-card" style="top:419px">
      <div class="thumb" role="img" aria-label="Hand touching a glowing education icon" style="background:linear-gradient(135deg,#2a4f86,#5a88c4 55%,#1c2f55)"></div>
      <h4>3.1: Parallel Lines and Transversals</h4>
      <p>Career Spotlight: Transportation Engineers, Electrical Power-line Repairers, Structural Metal Fabricator, Fence Erectors</p>
      <span class="due">Due : 10/15 at 11:59 PM</span><span class="btn">Begin Lesson</span>
      <svg class="gear" width="13" height="13" viewBox="0 0 24 24"><path fill="#333" d="M12 8a4 4 0 1 0 0 8a4 4 0 0 0 0-8zm9.4 5.5l2.1 1.6-2 3.5-2.5-1a8 8 0 0 1-2.3 1.3L16.3 22h-4l-.4-2.6a8 8 0 0 1-2.3-1.3l-2.5 1-2-3.5 2.1-1.6a8 8 0 0 1 0-2.6L5.1 9.8l2-3.5 2.5 1a8 8 0 0 1 2.3-1.3L12.3 3h4l.4 2.6a8 8 0 0 1 2.3 1.3l2.5-1 2 3.5-2.1 1.6a8 8 0 0 1 0 2.6z" transform="translate(-2.3 -0.5)"/></svg>
    </article>
    <article class="lesson-card" style="top:529px">
      <div class="thumb" role="img" aria-label="Colleagues meeting in an office" style="background:linear-gradient(135deg,#4a4e55,#9da2a8 55%,#e2e2e2)"></div>
      <h4>3.3: Angle Relationships in Triangles</h4>
      <p>Career Spotlight: Geodetic Surveyors, Precious Metal Workers, Marketing Manager, Roofer, Textile Knitting Machine Setter</p>
      <span class="due">Due : 10/15 at 11:59 PM</span><span class="btn">Begin Lesson</span>
      <svg class="gear" width="13" height="13" viewBox="0 0 24 24"><path fill="#333" d="M12 8a4 4 0 1 0 0 8a4 4 0 0 0 0-8zm9.4 5.5l2.1 1.6-2 3.5-2.5-1a8 8 0 0 1-2.3 1.3L16.3 22h-4l-.4-2.6a8 8 0 0 1-2.3-1.3l-2.5 1-2-3.5 2.1-1.6a8 8 0 0 1 0-2.6L5.1 9.8l2-3.5 2.5 1a8 8 0 0 1 2.3-1.3L12.3 3h4l.4 2.6a8 8 0 0 1 2.3 1.3l2.5-1 2 3.5-2.1 1.6a8 8 0 0 1 0 2.6z" transform="translate(-2.3 -0.5)"/></svg>
    </article>
  </section>

  <section class="promo">
    <h2>SUF Assessments Looking for your<br>upcoming SUF Assessments?</h2>
    <p>The SUF Assessments are designed to be taken 3 times a year at the beginning of the year, the middle of the year, and the end of the year. Navigate over to SUF Assessments now to see what's coming up!</p>
    <span class="btn">Go there &nbsp;now</span>
    <div class="promo-media" role="img" aria-label="Hand reaching toward a glowing digital assessment dial"></div>
  </section>

  <footer class="site-footer" style="height:112px">
    <div class="links"><span style="left:298px;top:38px">HOME</span><span style="left:381px;top:38px">CAREER TOOLS</span><span style="left:519px;top:38px">CLASSES</span><span style="left:617px;top:38px">ASSESSMENTS</span></div>
    <div class="copy" style="top:72px">Copyright © 2021 All Rights Reserved</div>
  </footer>
</main>

</body>
</html>
```